fernbolt website

commerce website to sell cookeries, brackets, mailboxes and to show off homes built. Modern Steel in design see kelvo rides web page to be like: https://www.kelvorides.com/en/ sorry its blue mantis hosting word press divi

must be able to add products to page

Target Market(s)

mainly western states of U.S.

Industry/Entity Type

Building Product

Coding

Coded - Design and coding required

Number of Pages Required

3 page

Font styles to use
Sans Serif

Colors

Designer to choose colors to be used in the design.

Requirements
Must have
• customers to be able to order products from page
• blue mantis hosting word press divi

```html
<!DOCTYPE html>
<html lang="en">
<head>
<meta charset="utf-8">
<title>Fernbolt – Contact Us</title>
<link href="https://fonts.googleapis.com/css2?family=Poppins:wght@300;400;500;600&display=swap" rel="stylesheet">
<style>
:root{
  --brand:#445e88;
  --brand-dark:#3a5178;
  --ink:#111418;
  --muted:#555b63;
  --line:#c9ccd2;
  --band:#f2f2f2;
  --white:#fff;
}
*{box-sizing:border-box;margin:0;padding:0}
html,body{width:683px;height:1200px;overflow:hidden;background:#fff}
body{font-family:'Poppins',sans-serif;color:var(--ink);position:relative}
.abs{position:absolute}
.topbar{left:0;top:0;width:683px;height:23px;background:var(--brand);color:#fff;font-size:7px;display:flex;align-items:center;justify-content:space-between;padding:0 50px}
.topbar .cur{display:flex;align-items:center;gap:4px}
.topbar .cur i{width:12px;height:12px;border-radius:50%;background:#fff;display:inline-block}
.header{left:0;top:23px;width:683px;height:56px;border-bottom:1px solid #e6e6e6}
.brandname{left:50px;top:20px;font-size:12px;font-weight:500;color:var(--brand);letter-spacing:.5px;display:flex;align-items:center;gap:6px}
.brandname i{width:12px;height:12px;background:var(--brand);display:inline-block}
.search{left:259px;top:16px;width:238px;height:24px;border:1px solid #d8d8d8;border-radius:12px;font-size:7px;color:#555;display:flex;align-items:center}
.search .cat{width:80px;padding-left:11px;border-right:1px solid #ddd;line-height:14px}
.search .q{padding-left:9px;color:#999;flex:1}
.search .btn{width:18px;height:18px;border-radius:50%;background:#e3e3e3;margin-right:3px;display:flex;align-items:center;justify-content:center}
.hicons{left:520px;top:24px;display:flex;align-items:center;gap:18px;font-size:8px;font-weight:600}
.badge{position:absolute;left:12px;top:2px;width:10px;height:10px;border-radius:50%;background:var(--brand);color:#fff;font-size:6px;text-align:center;line-height:10px}
.nav{left:0;top:79px;width:683px;height:28px;display:flex;justify-content:center;gap:21px;font-size:7px;font-weight:500;align-items:center}
.nav span{position:relative}
.nav .active{color:var(--brand)}
.nav .active:before{content:"";position:absolute;left:0;right:0;top:-14px;height:1.5px;background:var(--brand)}
.titleband{left:0;top:107px;width:683px;height:75px;background:var(--band)}
.titleband h1{position:absolute;left:50px;top:26px;font-size:19px;font-weight:400;letter-spacing:.5px}
.crumb{position:absolute;right:50px;top:32px;font-size:8px;display:flex;gap:8px;align-items:center}
.card{left:51px;top:233px;width:267px;height:278px;background:#fff;box-shadow:0 6px 22px rgba(0,0,0,.09)}
.card h2{position:absolute;left:18px;top:22px;font-size:15px;font-weight:500}
.card .sub{position:absolute;left:19px;top:43px;font-size:7px}
.field{position:absolute;left:19px;width:224px;border-bottom:1px solid #888;font-size:7px;padding-bottom:6px}
.send{position:absolute;right:21px;top:248px;font-size:8.5px;font-weight:600;letter-spacing:.8px;color:var(--brand);border-bottom:1.5px solid var(--brand);padding-bottom:1px}
.touch{left:367px;top:250px;width:266px}
.touch h2{font-size:22px;font-weight:300;letter-spacing:.5px;margin-bottom:6px}
.item{display:flex;gap:7px;margin-top:9px}
.item svg{flex:none;margin-top:1px}
.item b{display:block;font-size:8px;font-weight:600}
.item p{font-size:9px;color:var(--muted);font-weight:300;margin-top:1px}
.sep{height:1px;background:#e6e6e6;margin:13px 0 10px 2px}
.socials{display:flex;gap:5px;margin-top:23px;margin-left:1px}
.socials i{width:19px;height:19px;border-radius:50%;display:block}
.map{left:51px;top:574px;width:581px;height:252px;background:linear-gradient(135deg,#e4e4e4,#d6d6d6)}
.mapnote{left:265px;top:688px;width:153px;height:60px;border-radius:30px;background:#fff;text-align:center;box-shadow:0 2px 8px rgba(0,0,0,.08)}
.mapnote b{display:block;font-size:9px;font-weight:500;margin-top:9px}
.mapnote p{font-size:6.5px;margin-top:4px;line-height:10px}
.footer{left:0;top:929px;width:683px;height:271px;background:var(--brand);color:#fff}
.news{left:377px;top:887px;width:306px;height:82px;background:var(--brand-dark)}
.news .in{position:absolute;left:48px;top:26px;width:181px;height:31px;background:#fff;font-size:7px;color:#444;display:flex;align-items:center;padding-left:10px;gap:6px}
.news .go{position:absolute;left:229px;top:26px;width:26px;height:31px;background:var(--brand);display:flex;align-items:center;justify-content:center}
.fname{left:50px;top:1085px;font-size:18px;font-weight:500;color:#fff;letter-spacing:.5px;display:flex;align-items:center;gap:8px}
.fname i{width:16px;height:16px;border:2px solid #fff;border-radius:50%;display:block}
.col{font-size:7px;line-height:15px}
.col h3{font-size:8.5px;font-weight:500;letter-spacing:.3px;margin-bottom:7px}
.ci{display:flex;gap:6px;line-height:10px;margin-bottom:10px}
.fsoc{display:flex;gap:4px}
.fsoc i{width:17px;height:17px;border-radius:50%;background:#52698f;display:block}
.pay{display:flex;gap:5px}
.pay i{width:28px;height:18px;border-radius:3px;background:#fff;display:block}
.rule{left:50px;top:1167px;width:582px;height:1px;background:#5d7398}
.copy{left:0;top:1180px;width:683px;text-align:center;font-size:7px;color:#fff}
.up{left:644px;top:1157px;width:23px;height:23px;border-radius:50%;background:#fff;display:flex;align-items:center;justify-content:center}
</style>
</head>
<body>
<div class="abs topbar"><span>FREE SHIPPING WORLDWIDE for orders over £20</span><span class="cur"><i></i>Dollar (Us) ⌄</span></div>

<div class="abs header">
  <div class="abs brandname"><i></i>FERNBOLT</div>
  <div class="abs search"><span class="cat">All Categories</span><span class="q">Search for products</span><span class="btn"><svg width="8" height="8" viewBox="0 0 10 10"><circle cx="4" cy="4" r="3" fill="none" stroke="#555" stroke-width="1.2"/><path d="M6.5 6.5 9 9" stroke="#555" stroke-width="1.2"/></svg></span></div>
  <div class="abs hicons">
    <svg width="11" height="11" viewBox="0 0 12 12"><path d="M2 6a4 4 0 0 1 7-2.6M10 6a4 4 0 0 1-7 2.6" fill="none" stroke="#333" stroke-width="1"/><path d="M9 1v2.5H6.5M3 11V8.5h2.5" fill="none" stroke="#333" stroke-width="1"/></svg>
    <svg width="11" height="10" viewBox="0 0 12 11"><path d="M6 10 1.5 5.5a2.6 2.6 0 0 1 4.5-3 2.6 2.6 0 0 1 4.5 3z" fill="none" stroke="#333" stroke-width="1"/></svg>
    <span style="position:relative;display:flex;gap:14px;align-items:center"><svg width="12" height="11" viewBox="0 0 12 11"><path d="M0 1h2l1.5 6h6.5l1.5-4.5H3" fill="none" stroke="#333" stroke-width="1"/><circle cx="4.5" cy="9.5" r=".9" fill="#333"/><circle cx="9" cy="9.5" r=".9" fill="#333"/></svg><span class="badge">4</span><span><sup style="font-size:5px">$</sup>458.36</span></span>
  </div>
</div>

<nav class="abs nav"><span>HOME</span><span>WHO WE ARE</span><span>ACCESSORIES</span><span>PRODUCT</span><span>FEATURED</span><span>SHOP</span><span>BLOG</span><span>SHIPPING &amp; DELIVERY</span><span class="active">CONTACT US</span></nav>

<section class="abs titleband"><h1>CONTACT US</h1><div class="crumb"><svg width="10" height="8" viewBox="0 0 10 8"><path d="M5 0 0 4h1.3v4h2.7V5.5h2V8h2.7V4H10z" fill="#888"/></svg><span>Home</span><span>|</span><span>Contact Us</span></div></section>

<section class="abs card">
  <h2>REACH TO US</h2>
  <p class="sub">Contact us &amp; find how can benefit your company.</p>
  <div class="field" style="top:70px">Enter your name...</div>
  <div class="field" style="top:99px">Enter your Email..</div>
  <div class="field" style="top:127px">Enter your Phone Number...</div>
  <div class="field" style="top:156px">Enter your Subject...</div>
  <div class="field" style="top:189px;height:40px">Enter your Message...</div>
  <span class="send">SEND MESSAGE</span>
</section>

<section class="abs touch">
  <h2>GET IN TOUCH</h2>
  <div class="item"><svg width="9" height="9" viewBox="0 0 10 10"><path d="M2 0 4 2.5 3 4a6 6 0 0 0 3 3l1.5-1L10 8 8.5 10C4 9.5.5 6 0 1.5z" fill="var(--brand)"/></svg><div><b>PHONE</b><p>(+08) 123 456 7890</p></div></div>
  <div class="item"><svg width="9" height="10" viewBox="0 0 8 11"><path d="M4 0a4 4 0 0 1 4 4c0 3-4 7-4 7S0 7 0 4a4 4 0 0 1 4-4z" fill="var(--brand)"/><circle cx="4" cy="4" r="1.5" fill="#fff"/></svg><div><b>ADDRESS</b><p>Some address line goes here city name country name</p></div></div>
  <div class="item"><svg width="10" height="9" viewBox="0 0 10 9"><rect x="2.5" y="0" width="5" height="3" fill="var(--brand)"/><rect x="0" y="3" width="10" height="4" fill="var(--brand)"/><rect x="2.5" y="6" width="5" height="3" fill="#fff" stroke="var(--brand)"/></svg><div><b>FAX</b><p>(864) 123-456-789</p></div></div>
  <div class="sep"></div>
  <div class="item"><svg width="9" height="9" viewBox="0 0 10 10"><path d="M2 0 4 2.5 3 4a6 6 0 0 0 3 3l1.5-1L10 8 8.5 10C4 9.5.5 6 0 1.5z" fill="var(--brand)"/></svg><div><b>PHONE</b><p>(+08) 123 456 7890</p></div></div>
  <div class="item"><svg width="9" height="10" viewBox="0 0 8 11"><path d="M4 0a4 4 0 0 1 4 4c0 3-4 7-4 7S0 7 0 4a4 4 0 0 1 4-4z" fill="var(--brand)"/><circle cx="4" cy="4" r="1.5" fill="#fff"/></svg><div><b>ADDRESS</b><p>Some address line goes here city name country name</p></div></div>
  <div class="socials"><i style="background:#3b5998"></i><i style="background:#1da1f2"></i><i style="background:#dd4b39"></i><i style="background:#c13584"></i><i style="background:#e62117"></i></div>
</section>

<div class="abs map" role="img" aria-label="Street map of the surrounding area with a location pin"></div>
<svg class="abs" style="left:334px;top:651px" width="16" height="21" viewBox="0 0 16 21"><path d="M8 0a8 8 0 0 1 8 8c0 6-8 13-8 13S0 14 0 8a8 8 0 0 1 8-8z" fill="var(--brand)"/><circle cx="8" cy="8" r="3" fill="#fff"/></svg>
<div class="abs mapnote"><b>Address</b><p>Some Address line goes here, city<br>name, country name here.</p></div>

<footer class="abs footer"></footer>
<div class="abs news"><div class="in"><svg width="7" height="5" viewBox="0 0 7 5"><rect width="7" height="5" fill="#bbb"/><path d="M0 0l3.5 2.5L7 0" stroke="#fff" fill="none" stroke-width=".6"/></svg>Enter your email address...</div><div class="go"><svg width="8" height="8" viewBox="0 0 10 10"><path d="M10 0 0 4l3.5 1.5L9 1 4.5 6.5V10L6 7l2.5 1.5z" fill="#fff"/></svg></div></div>

<div class="abs fname"><i></i>FERNBOLT</div>
<div class="abs col" style="left:236px;top:1020px;color:#fff"><h3>INFORMATION</h3>About Us<br>Delivery<br>Store<br>Terms &amp; Conditions<br>Policies<br>Shop Instagram</div>
<div class="abs col" style="left:363px;top:1020px;color:#fff"><h3>CONTACT US</h3>
  <div class="ci"><svg width="7" height="6" viewBox="0 0 7 5"><rect width="7" height="5" fill="#fff"/><path d="M0 0l3.5 2.5L7 0" stroke="var(--brand)" fill="none" stroke-width=".6"/></svg><span>Email:<br>hello@fernbolt-demo.com</span></div>
  <div class="ci"><svg width="8" height="8" viewBox="0 0 10 10"><path d="M2 0 4 2.5 3 4a6 6 0 0 0 3 3l1.5-1L10 8 8.5 10C4 9.5.5 6 0 1.5z" fill="#fff"/></svg><span>Phone:<br>123-456-7890</span></div>
  <div class="ci"><svg width="6" height="8" viewBox="0 0 8 11"><path d="M4 0a4 4 0 0 1 4 4c0 3-4 7-4 7S0 7 0 4a4 4 0 0 1 4-4z" fill="#fff"/></svg><span>Office Location:<br>Some address line goes here</span></div>
</div>
<div class="abs col" style="left:503px;top:1020px;color:#fff"><h3>LET'S GET SOCIAL</h3><div class="fsoc"><i></i><i></i><i></i></div><h3 style="margin-top:18px">PAYMENT METHODS</h3><div class="pay"><i></i><i style="background:#1a3e9a"></i><i style="background:#222"></i><i></i></div></div>

<div class="abs rule"></div>
<div class="abs copy">© 2020. FERNBOLT. ALL RIGHTS RESERVED</div>
<div class="abs up"><svg width="7" height="8" viewBox="0 0 7 8"><path d="M3.5 8V1M1 3.5l2.5-2.5L6 3.5" fill="none" stroke="#222" stroke-width=".8"/></svg></div>
</body>
</html>
```